Structural Engineering Company needs ad for magazine

We are an engineering office for structural engineering in the entertainment industry. Our focus are concert stages, festival structures, grand stands and exhibition booths. Our customers are mainly from Europe, we realize the projects worldwide. Typical customers are designer, architects, stage builders, exhibition builder and technical service provider. We are creating structural analyses, technical consulting, technical drawings and risk assessment. We are working on mid size and major events.
Some technical notes:
- CMYK profile needed, minimum 300 dpi for raster graphic
- Our primary color is Petrol. Favourite is petrol, coral and grey (black). Please use palette shown below.
- Our font in documents is Myriad. Regular at 10 pt for text and Light at 16-24pt for titles.
- The format for the ad is 61 x 127 mm (portrait) or 185 x 46 mm (landscape). Which one is up to you.
To the content:
- For contact details we just want to provide our web address "falkowerk.de" and/or our e-mail "info@falkowerk.de"
- Attached are some Logo files and photos.
- The ad do not advertise a specific product. It is more a general advertisement for the company.
- The language for the ad should be German. Below are keywords in English and corresponding German translation. You do not need to place all Keywords, it is just a brainstorming list to help you. You are also welcome to use other text. We will help with translation, if necessary.
- we like discussing ideas to get better results, so also if you have questions, please ask.
- If you need information that we haven't thought of yet, please ask.
Our slogan (also in Germany): event meets engineering
Service Keywords EN / DE
- Structural Analysis / Statische Berechnungen
- Risk Assessment / Risikobewertungen
- Consulting & Design / Beratung & Konstruktion
Technical Keywords EN / DE
- Stage machinery / Bühnentechnik
- Scaffolding / Gerüstbau
- Exhibition Booths / Messebauten
- Tents / Zelte
- Temporary Structures / Fliegende Bauten
- Truss / Traversen
- Stages / Bühnen
- Grand Stands / Tribünen
- Leightweight Construction / Leichtbau
- Steel Construction / Stahlbau
- Amusement Rides / Fahrgeschäfte
Look and feel

```html
<!DOCTYPE html>
<html lang="de">
<head>
<meta charset="utf-8">
<title>Falkowerk – Statische Berechnungen</title>
<link href="https://fonts.googleapis.com/css2?family=Bebas+Neue&family=Poppins:wght@400;500;600&display=swap" rel="stylesheet">
<style>
  :root {
    --bg: #dcdcdc;
    --white: #ffffff;
    --ink: #1b1b1b;
    --text: #2a2a2a;
    --petrol: #2ab3cc;
    --coral: #ef7a88;
    --lavender: #8a9dd6;
    --ochre: #d7a35a;
    --panel-grey: #c9c9c9;
    --frame-grey: #bdbdbd;
  }
  * { margin: 0; padding: 0; box-sizing: border-box; }
  html, body { width: 1200px; height: 2400px; overflow: hidden; background: var(--bg); }
  .ad {
    position: absolute; left: 104px; top: 168px;
    width: 992px; height: 2064px; background: var(--white); overflow: hidden;
    font-family: "Poppins", sans-serif;
  }

  /* Hero */
  .hero {
    position: absolute; left: 0; top: 0; width: 992px; height: 744px;
    background:
      radial-gradient(ellipse 150px 120px at 620px 730px, rgba(235,225,255,.85), rgba(170,150,235,0)),
      radial-gradient(ellipse 110px 90px at 760px 720px, rgba(225,215,255,.7), rgba(170,150,235,0)),
      radial-gradient(ellipse 140px 110px at 650px 560px, rgba(200,190,250,.6), rgba(150,130,230,0)),
      radial-gradient(ellipse 360px 330px at 640px 600px, rgba(120,80,200,.85), rgba(90,45,150,0) 80%),
      radial-gradient(circle 70px at 845px 50px, rgba(255,90,140,.95), rgba(240,80,120,0)),
      radial-gradient(circle 65px at 800px 170px, rgba(255,90,140,.85), rgba(240,80,120,0)),
      radial-gradient(ellipse 300px 200px at 150px 140px, rgba(170,40,110,.75), rgba(170,40,110,0)),
      radial-gradient(ellipse 260px 300px at 920px 420px, rgba(60,40,90,.9), rgba(60,40,90,0)),
      linear-gradient(180deg, #5a1d4e 0%, #3a1436 40%, #2a1034 70%, #3a1f52 100%);
  }
  .hero-bubble { position: absolute; left: 0; top: 0; }
  .brand {
    position: absolute; left: 501px; top: 112px; transform: translateX(-50%);
    display: flex; align-items: center; gap: 12px; white-space: nowrap;
  }
  .brand-mark { width: 20px; height: 20px; background: var(--ink); }
  .brand-name {
    font-weight: 600; font-size: 32px; letter-spacing: 5px; color: var(--ink);
  }
  .hero-title {
    position: absolute; left: 51px; top: 258px;
    font-family: "Bebas Neue", sans-serif; font-weight: 400;
    font-size: 94px; line-height: 102px; color: var(--white);
  }
  .hero-rule {
    position: absolute; left: 52px; top: 470px; width: 286px; height: 3px;
    background: linear-gradient(90deg, #fff 65%, rgba(255,255,255,.2));
  }
  .slogan {
    position: absolute; left: 52px; top: 493px;
    font-size: 25px; line-height: 34px; color: var(--white); font-weight: 400;
  }
  .stripe { position: absolute; left: 0; height: 45px; }
  .stripe-1 { top: 556px; width: 400px; background: linear-gradient(90deg, rgba(42,179,204,.95) 55%, rgba(42,179,204,.6)); clip-path: polygon(0 0, 345px 0, 100% 100%, 0 100%); }
  .stripe-2 { top: 608px; width: 520px; background: linear-gradient(90deg, rgba(42,179,204,.95) 45%, rgba(42,179,204,.1)); }
  .stripe-3 { top: 660px; width: 700px; background: linear-gradient(90deg, rgba(42,179,204,.95) 35%, rgba(42,179,204,.05)); }

  /* Service tiles */
  .services { position: absolute; left: 0; top: 744px; width: 992px; height: 596px; }
  .service { position: absolute; width: 496px; height: 298px; overflow: hidden; }
  .service-photo { position: absolute; inset: 0; }
  .service-label {
    position: absolute; left: 0; bottom: 0; height: 80px;
    font-family: "Bebas Neue", sans-serif; font-weight: 400;
    font-size: 70px; line-height: 86px; color: var(--white);
    padding-left: 21px; white-space: nowrap;
  }
  .service--stage { left: 0; top: 0; }
  .service--stage .service-photo {
    background:
      radial-gradient(ellipse 140px 110px at 430px 170px, rgba(240,240,255,.95), rgba(180,190,240,0)),
      radial-gradient(ellipse 240px 90px at 300px 60px, rgba(215,215,225,.8), rgba(200,200,215,0)),
      radial-gradient(ellipse 200px 140px at 90px 210px, rgba(150,70,180,.8), rgba(120,60,170,0)),
      linear-gradient(160deg, #7a4ab8 0%, #3a2a70 45%, #5a4aa8 75%, #2a2050 100%);
  }
  .service--stage .service-label { width: 418px; background: var(--petrol); clip-path: polygon(0 0, 394px 0, 100% 100%, 0 100%); }

  .service--scaffold { left: 496px; top: 0; }
  .service--scaffold .service-photo {
    background:
      radial-gradient(ellipse 160px 80px at 380px 40px, rgba(250,250,250,1), rgba(240,240,240,0)),
      linear-gradient(180deg, rgba(0,0,0,0) 55%, #2a7fae 72%, #3ab0c8 85%, #2a6a90 100%),
      linear-gradient(90deg, #6a6e74 0%, #b8bcc2 35%, #9aa0a8 60%, #c8ccd0 100%);
  }
  .service--scaffold .service-label { width: 421px; background: var(--coral); clip-path: polygon(0 0, 397px 0, 100% 100%, 0 100%); }

  .service--booth { left: 0; top: 298px; }
  .service--booth .service-photo {
    background:
      radial-gradient(ellipse 110px 110px at 190px 140px, rgba(235,205,160,1), rgba(220,185,135,0)),
      radial-gradient(ellipse 110px 120px at 370px 150px, rgba(225,195,150,.95), rgba(215,180,130,0)),
      linear-gradient(180deg, #3f7a2e 0%, #5c9a3e 25%, #b8a070 55%, #c9a878 75%, #7a7a72 100%);
  }
  .service--booth .service-label { width: 418px; background: var(--lavender); clip-path: polygon(0 0, 394px 0, 100% 100%, 0 100%); }

  .service--temporary { left: 496px; top: 298px; }
  .service--temporary .service-photo {
    background:
      radial-gradient(ellipse 200px 60px at 250px 15px, rgba(200,205,210,.8), rgba(200,205,210,0)),
      linear-gradient(180deg, #8a9098 0%, #4a4e56 25%, #3a3e46 45%, rgba(58,62,70,0) 60%),
      linear-gradient(180deg, #3a3e46 0%, #2a5e88 70%, #3aa0c0 85%, #c8ccd0 100%);
  }
  .service--temporary .service-label { width: 457px; background: var(--ochre); clip-path: polygon(0 0, 433px 0, 100% 100%, 0 100%); }

  /* Planning */
  .planning { position: absolute; left: 0; top: 1340px; width: 992px; height: 724px; background: var(--white); }
  .planning-side { position: absolute; left: 725px; top: 0; width: 267px; height: 724px; background: var(--panel-grey); }
  .planning-frame {
    position: absolute; left: 422px; top: 50px; width: 564px; height: 539px;
    background: var(--frame-grey); padding: 11px;
  }
  .planning-photo {
    width: 100%; height: 100%;
    background:
      linear-gradient(155deg, rgba(42,179,204,0) 58%, rgba(42,179,204,.5) 78%, rgba(42,179,204,.3) 100%),
      linear-gradient(172deg, rgba(220,235,60,0) 58%, rgba(220,235,60,.75) 63%, rgba(220,235,60,.75) 68%, rgba(220,235,60,0) 73%),
      linear-gradient(180deg, #3a3a3a 0%, #5a5a5c 14%, #2e2e30 22%, #303032 30%, #eeeeea 34%, #f4f4f0 100%);
  }
  .planning-title {
    position: absolute; left: 51px; top: 41px;
    font-family: "Bebas Neue", sans-serif; font-weight: 400;
    font-size: 88px; line-height: 86px; color: var(--lavender);
  }
  .planning-rule {
    position: absolute; left: 54px; top: 233px; width: 186px; height: 4px;
    background: linear-gradient(90deg, var(--ink), rgba(27,27,27,.35));
  }
  .planning-text {
    position: absolute; left: 45px; width: 380px;
    font-size: 21px; line-height: 27.5px; color: var(--text); white-space: nowrap;
  }
  .planning-text--intro { top: 264px; }
  .planning-text--focus { top: 423px; }
  .contact {
    position: absolute; left: 45px; top: 626px;
    display: flex; align-items: center; gap: 14px;
  }
  .contact-url { font-size: 46px; line-height: 52px; font-weight: 500; color: var(--ink); }
</style>
</head>
<body>
<div class="ad">
  <section class="hero" role="img" aria-label="Nahaufnahme eines Bühnenscheinwerfers in violettem Licht">
    <svg class="hero-bubble" width="992" height="230" viewBox="0 0 992 230">
      <path d="M200 0 C260 0 272 30 300 95 C335 170 410 217 501 217 C592 217 667 170 702 95 C730 30 742 0 802 0 Z" fill="#ffffff"/>
    </svg>
    <div class="brand">
      <span class="brand-mark"></span>
      <span class="brand-name">FALKOWERK</span>
    </div>
    <h1 class="hero-title">Statische<br>Berechnungen</h1>
    <div class="hero-rule"></div>
    <p class="slogan">Event Meets Engineering</p>
    <div class="stripe stripe-1"></div>
    <div class="stripe stripe-2"></div>
    <div class="stripe stripe-3"></div>
  </section>

  <section class="services">
    <div class="service service--stage">
      <div class="service-photo" role="img" aria-label="Aluminium-Traverse mit Scheinwerfern über einer Bühne"></div>
      <h2 class="service-label">Bühnentechnik</h2>
    </div>
    <div class="service service--scaffold">
      <div class="service-photo" role="img" aria-label="Gerüstkonstruktion in einem Stadion"></div>
      <h2 class="service-label">Gerüstbau</h2>
    </div>
    <div class="service service--booth">
      <div class="service-photo" role="img" aria-label="Holzpavillons und Kuppel auf einem Ausstellungsgelände"></div>
      <h2 class="service-label">Messebauten</h2>
    </div>
    <div class="service service--temporary">
      <div class="service-photo" role="img" aria-label="Bühnenaufbau aus Stahlgerüst in einem Stadion"></div>
      <h2 class="service-label">Fliegende Bauten</h2>
    </div>
  </section>

  <section class="planning">
    <div class="planning-side"></div>
    <div class="planning-frame">
      <div class="planning-photo" role="img" aria-label="Handskizze auf kariertem Papier mit einem Veranstaltungsarmband"></div>
    </div>
    <h2 class="planning-title">Technische<br>Planung</h2>
    <div class="planning-rule"></div>
    <p class="planning-text planning-text--intro">Manchmal hat man eine<br>gute Idee, aber die<br>technische Umsetzung ist<br>vielleicht nicht so gelungen.<br>Ich helfe Ihnen gerne weiter.</p>
    <p class="planning-text planning-text--focus">Im Bereich Rigging, Bühnen-<br>und Eventbau, mit den<br>Schwerpunkten Traversen- und<br>Gerüstbau, erstelle ich<br>Gutachten.</p>
    <div class="contact">
      <svg width="52" height="52" viewBox="0 0 56 56" aria-hidden="true">
        <g fill="none" stroke="#1b1b1b" stroke-width="3.5">
          <circle cx="26" cy="26" r="22"/>
          <ellipse cx="26" cy="26" rx="10" ry="22"/>
          <line x1="4" y1="26" x2="48" y2="26"/>
          <path d="M8 14 H44 M8 38 H44"/>
        </g>
        <path d="M36 36 L54 43 L46 46 L43 54 Z" fill="#1b1b1b" stroke="#fff" stroke-width="2"/>
      </svg>
      <span class="contact-url">www.falkowerk.de</span>
    </div>
  </section>
</div>
</body>
</html>
```